I am looking for a flyer design for my upcoming symposium. Here are the details for the flyer and pictures of speakers are attached.

Name of Symposium: Lattice and Pathway Biosciences Symposium, Sponsored by the Corvale Chromatin Institute and the Department of Bioengineering
Date: January 8, 2018
Location: Havergill Auditorium, Tarnby Center for Applied Discovery, 2175 Orchard Terrace Ave, Philadelphia, PA 19127

Reception to follow after the symposium.

Also, please add - Register and upload abstracts for the symposium at www.qzvmrk.com. Registration and abstract submission closes on January 4, 2018.

Keynote Speaker:
Marthe Quillon, Ph.D.
NTVO Director General; Professor, Lyceum of Norvane; Director, Genetics and Developmental Biology at Institut Bramoux
Lyceum of Norvane, NTVO, Institut Bramoux
"Title of talk TBA."

Speakers:
Lena Drewcott, Ph.D.
Assistant Professor of Cell and Developmental Biology
Halvering State University, HMCS
"Title of talk TBA."

Paul Marden, Ph.D.
Assistant Professor of Genetics
"Title of talk TBA."

Ilse Varga, Ph.D.
Professor, Ostrander University
Otto Wenzlau Center for Molecular Medicine
"Title of talk TBA."

Jun Hao, Ph.D.
Professor of Cellular and Molecular Medicine
Coastal Meridian University
"Title of talk TBA."

Wei Lun, Ph.D.
Associate Professor of Pediatrics
The Youth Medical Pavilion of Philadelphia
"Spatial genome re-organization between fetal and adult hematopoietic stem cells."

Mei Zhou, Ph.D.
Professor, Department of Genetics
Ellsworth Medical School
"Title of talk TBA."

```html
<!DOCTYPE html>
<html lang="en">
<head>
<meta charset="utf-8">
<title>Lattice and Pathway Biosciences Symposium – Flyer</title>
<link rel="stylesheet" href="https://fonts.googleapis.com/css2?family=Fira+Sans+Condensed:wght@600;700&family=Source+Sans+3:wght@400;600;700&family=PT+Sans:wght@700&display=swap">
<style>
:root{
  --stage:#e6e6e6;
  --paper:#ffffff;
  --navy:#213f7e;
  --blue:#2a74b5;
  --mid-blue:#2b5ea8;
  --sky:#a9cfee;
  --pale:#cfe3f5;
  --red:#d0283a;
  --title-navy:#1d3a7a;
  --grey-text:#555a60;
  --name-grey:#5a5f66;
  --white:#ffffff;
}
*{box-sizing:border-box;margin:0;padding:0}
html,body{width:1200px;height:848px;overflow:hidden}
body{background:var(--stage);font-family:"Source Sans 3",Arial,sans-serif;position:relative}
.page{position:absolute;top:74px;width:490px;height:692px;background:var(--paper);overflow:hidden}
.page--front{left:69px}
.page--back{left:626px}
.page__art{position:absolute;inset:0;width:490px;height:692px;z-index:0}
.page > :not(.page__art){z-index:1}

/* front */
.title{position:absolute;left:54px;top:86px;font-family:"Fira Sans Condensed",Arial Narrow,sans-serif;font-weight:700;color:var(--title-navy);line-height:.98}
.title__line{display:block;font-size:33px;letter-spacing:.5px}
.title__year{font-family:"Source Sans 3",Arial,sans-serif;font-weight:400;color:var(--red);font-size:24px;letter-spacing:14px;margin-left:6px;vertical-align:top}
.title__event{display:block;color:var(--red);font-family:"Source Sans 3",Arial,sans-serif;font-weight:400;font-size:34px;letter-spacing:22.5px;margin-top:2px}
.sponsors{position:absolute;left:43px;top:240px;width:118px;color:var(--title-navy)}
.sponsors__label{font-size:11.5px;letter-spacing:.2px}
.sponsor{display:flex;align-items:flex-start;gap:7px;margin-top:34px;font-size:14px;font-weight:600;color:var(--title-navy);line-height:1.05}
.sponsor__mark{width:13px;height:13px;background:var(--red);flex:none;margin-top:1px}
.sponsor + .sponsor{margin-top:24px}
.info{position:absolute;left:216px;color:var(--white);font-size:11px;line-height:1.3;font-weight:400}
.info--date{top:259px}
.info--location{top:320px;width:205px;line-height:14px}
.info--reception{top:405px}
.register{position:absolute;right:37px;top:575px;text-align:right;color:var(--white);font-size:19px;line-height:24px;font-weight:400}
.register__url{font-weight:700;font-size:18px;letter-spacing:.3px}
.deadline{position:absolute;left:42px;top:632px;width:196px;height:39px;background:var(--red);color:var(--white);font-size:11px;line-height:13.5px;text-align:center;padding-top:6px}

/* back */
.section-head{position:absolute;left:32px;font-family:"PT Sans",Arial,sans-serif;font-weight:700;font-size:18px;color:var(--title-navy);letter-spacing:.2px}
.section-head--keynote{top:83px}
.section-head--speakers{top:221px}
.portrait{position:absolute;clip-path:polygon(25% 0,75% 0,100% 50%,75% 100%,25% 100%,0 50%);background:linear-gradient(160deg,#b9a48e,#7c6a58)}
.speaker{position:absolute;color:var(--grey-text)}
.speaker__name{font-family:"PT Sans",Arial,sans-serif;font-weight:700;color:var(--name-grey);font-size:14.5px;line-height:14px}
.speaker__info{font-size:7.4px;line-height:9.6px;margin-top:1px}
.keynote{position:absolute;left:148px;top:120px;color:var(--grey-text)}
.keynote__name{font-family:"PT Sans",Arial,sans-serif;font-weight:700;color:var(--name-grey);font-size:19px}
.keynote__info{font-size:9.2px;line-height:15px;margin-top:2px}
</style>
</head>
<body>

<section class="page page--front">
  <svg class="page__art" viewBox="0 0 490 692" aria-hidden="true">
    <polygon points="0,0 490,0 490,100 0,50" fill="#2a74b5"/>
    <polygon points="110,0 490,0 490,72 350,58 185,74" fill="#213f7e"/>
    <polygon points="0,50 185,74 350,58 490,100 490,112 350,64 185,80 0,54" fill="#cfe3f5"/>
    <polygon points="17,67 490,80 490,262 430,195 40,190" fill="#a9cfee"/>
    <polygon points="40,190 430,195 445,208 50,200" fill="#2b5ea8"/>
    <rect x="20" y="440" width="350" height="125" rx="62" fill="#a9cfee" opacity=".35" role="img" aria-label="Molecule network decoration"/>
    <line x1="174" y1="238" x2="174" y2="445" stroke="#c8c8c8" stroke-width="2"/>
    <polygon points="168,252 368,252 373,279 168,279" fill="#d0283a"/>
    <polygon points="168,303 440,303 453,380 168,380" fill="#d0283a"/>
    <polygon points="168,399 455,399 463,426 168,426" fill="#d0283a"/>
    <polygon points="168,279 174,279 174,285" fill="#8d1d29"/>
    <polygon points="168,380 174,380 174,386" fill="#8d1d29"/>
    <polygon points="168,426 174,426 174,432" fill="#8d1d29"/>
    <g fill="none" stroke="#fff" stroke-width="1">
      <rect x="182" y="259" width="18" height="13" rx="1"/>
      <line x1="182" y1="263" x2="200" y2="263"/>
      <path d="M187 320a6 6 0 1 1 12 0c0 5-6 10-6 10s-6-5-6-10z"/>
      <circle cx="193" cy="320" r="2"/>
      <path d="M186 404l3 10 M194 404l-3 10 M189 414v6 M191 414v6"/>
    </g>
    <polygon points="0,600 490,430 490,470 0,640" fill="#d9e3f3"/>
    <polygon points="0,660 150,570 490,500 490,692 0,692" fill="#2b73b6"/>
    <polygon points="150,570 490,430 490,520" fill="#2b5ea8"/>
    <polygon points="0,692 0,630 120,605 260,692" fill="#213f7e"/>
    <circle cx="246" cy="592" r="18" fill="none" stroke="#fff" stroke-width="2"/>
    <polyline points="239,596 246,589 253,596" fill="none" stroke="#fff" stroke-width="2"/>
  </svg>

  <h1 class="title">
    <span class="title__line">LATTICE AND<span class="title__year">2018</span></span>
    <span class="title__line">PATHWAY BIOSCIENCES</span>
    <span class="title__event">SYMPOSIUM</span>
  </h1>

  <div class="sponsors">
    <p class="sponsors__label">SPONSORED BY</p>
    <p class="sponsor"><span class="sponsor__mark"></span><span>Brightwell<br>Engineering</span></p>
    <p class="sponsor"><span class="sponsor__mark"></span><span>Corvale<br>Chromatin<br>Institute</span></p>
  </div>

  <p class="info info--date">DATE: January 8, 2018</p>
  <p class="info info--location">LOCATION: Havergill Auditorium, Tarnby Center for Applied Discovery, 2175 Orchard Terrace Ave, Philadelphia, PA 19127</p>
  <p class="info info--reception">RECEPTION to follow after the symposium.</p>

  <p class="register">Register and upload<br>abstracts for<br>the symposium at<br><span class="register__url">www.qzvmrk.com</span></p>
  <p class="deadline">Registration and abstract submission closes on January 4, 2018.</p>
</section>

<section class="page page--back">
  <svg class="page__art" viewBox="0 0 490 692" aria-hidden="true">
    <polygon points="0,0 490,0 490,100 0,50" fill="#2a74b5"/>
    <polygon points="110,0 490,0 490,72 350,58 185,74" fill="#213f7e"/>
    <polygon points="0,50 185,74 350,58 490,100 490,112 350,64 185,80 0,54" fill="#cfe3f5"/>
    <rect x="350" y="150" width="130" height="140" rx="55" fill="#a9cfee" opacity=".25" role="img" aria-label="Molecule network decoration"/>
    <rect x="30" y="570" width="330" height="60" rx="30" fill="#a9cfee" opacity=".35" role="img" aria-label="Molecule network decoration"/>
    <polygon points="0,645 490,560 490,692 0,692" fill="#d9e3f3"/>
    <polygon points="0,672 300,622 490,575 490,692 0,692" fill="#2b73b6"/>
    <polygon points="300,622 490,548 490,578" fill="#2b5ea8"/>
    <polygon points="0,692 0,662 150,635 330,692" fill="#213f7e"/>
  </svg>

  <h2 class="section-head section-head--keynote">KEYNOTE SPEAKER</h2>
  <div class="portrait" style="left:19px;top:118px;width:94px;height:84px" role="img" aria-label="Portrait photo of Marthe Quillon"></div>
  <div class="keynote">
    <p class="keynote__name">Marthe Quillon, Ph.D.</p>
    <p class="keynote__info">NTVO Director General; Professor, Lyceum of Norvane; Director,<br>Genetics and Developmental Biology at Institut Bramoux<br>Lyceum of Norvane, NTVO, Institut Bramoux<br>"Title of talk TBA."</p>
  </div>

  <h2 class="section-head section-head--speakers">SPEAKERS</h2>

  <div class="portrait" style="left:27px;top:258px;width:82px;height:80px" role="img" aria-label="Portrait photo of Lena Drewcott"></div>
  <div class="speaker" style="left:120px;top:266px">
    <p class="speaker__name">Lena Drewcott,<br>Ph.D.</p>
    <p class="speaker__info">Assistant Professor of Cell and<br>Developmental Biology<br>Halvering State University, HMCS<br>"Title of talk TBA."</p>
  </div>

  <div class="portrait" style="left:245px;top:258px;width:92px;height:80px" role="img" aria-label="Portrait photo of Paul Marden"></div>
  <div class="speaker" style="left:348px;top:267px">
    <p class="speaker__name">Paul Marden,<br>Ph.D.</p>
    <p class="speaker__info">Assistant Professor of Genetics<br>Halvering State University, HMCS<br>"Title of talk TBA."</p>
  </div>

  <div class="portrait" style="left:21px;top:362px;width:90px;height:78px" role="img" aria-label="Portrait photo of Ilse Varga"></div>
  <div class="speaker" style="left:124px;top:371px">
    <p class="speaker__name">Ilse Varga,<br>Ph.D.</p>
    <p class="speaker__info">Professor, Ostrander University<br>Otto Wenzlau Center for Molecular<br>Medicine<br>"Title of talk TBA."</p>
  </div>

  <div class="portrait" style="left:246px;top:360px;width:90px;height:80px" role="img" aria-label="Portrait photo of Jun Hao"></div>
  <div class="speaker" style="left:350px;top:371px">
    <p class="speaker__name">Jun Hao,<br>Ph.D.</p>
    <p class="speaker__info">Professor of Cellular and<br>Molecular Medicine<br>Coastal Meridian University<br>"Title of talk TBA."</p>
  </div>

  <div class="portrait" style="left:21px;top:466px;width:90px;height:80px" role="img" aria-label="Portrait photo of Wei Lun"></div>
  <div class="speaker" style="left:123px;top:470px">
    <p class="speaker__name">Wei Lun,<br>Ph.D.</p>
    <p class="speaker__info">Associate Professor of Pediatrics<br>The Youth Medical Pavilion of<br>Philadelphia<br>"Spatial genome re-organization<br>between fetal and adult<br>hematopoietic stem cells."</p>
  </div>

  <div class="portrait" style="left:246px;top:463px;width:90px;height:80px" role="img" aria-label="Portrait photo of Mei Zhou"></div>
  <div class="speaker" style="left:353px;top:484px">
    <p class="speaker__name">Mei Zhou,<br>Ph.D.</p>
    <p class="speaker__info">Professor, Department of Genetics<br>Ellsworth Medical School<br>"Title of talk TBA."</p>
  </div>
</section>

</body>
</html>
```